Certified Probate & Trust Postcard

Hi, I am looking for your assistance. I need a postcard design based on the following specifications. The postcard needs to be 6x9. Here are the specifications for the front and back sides. I also need help incorporating a section on the front of the postcard where I can write the name or names of the people I am addressing the postcard to, as well as a space on the back for the stamp and the receiver's address.

(revised 6/18/2025)
🖼️ FRONT SIDE

(Visual: A serene Bay Area home or warm, sunlit interior. Include Tessa’s headshot. Color palette: ivory, slate, soft gold.)

Headline:

You’ve Taken On So Much — Let Me Help with What Comes Next

Subhead:

Strategic Real Estate Guidance for Probate & Trust
Certified Probate & Trust Specialist | Serving the San Francisco Bay Area

⸻

đź“© BACK SIDE

Opening Quote (italicized):

“I lost both of my parents in 2020 — just weeks apart. That experience shaped how I serve every estate I touch.”

⸻

Main Body Copy:

My name is Tessa Varden, and I’m a Certified Probate & Trust Specialist who works with families, attorneys, and fiduciaries to guide the real estate side of probate with structure, sensitivity, and strategy.

Whether you’re navigating this with legal support or filing in pro per, this process is layered — emotional, procedural, and often overwhelming. I provide a steady hand when everything else feels uncertain.

With over a decade of experience supporting executives at Corvane, Lumirel, and Dunmore Pike, I bring the same operational precision and discretion to every estate I manage. But I also bring empathy — because I’ve been in your shoes.

⸻

What I Offer — At No Upfront Cost to the Estate:
• Property clean-outs, inspections, and basic preparation — coordinated and covered
• Real estate strategy aligned with court timelines and estate goals
• Hands-on collaboration with attorneys or step-by-step guidance for independent petitioners
• Thoughtful communication that honors your time and your grief

Because real estate isn’t just business.
For you, it’s personal. For me, it’s both.

⸻

Call to Action (in soft gold frame or slate border):

If you’re managing a probate or trust estate and need support you can trust — let’s make this easier, together.
Instagram: @itstessavoo | LinkedIn: profilehub.net/in/tessahomesagent

Industry/Entity Type

Real Estate

Requirements
Must have
• Image needs to have a calm aesthetic (remember the person receiving is grieving) emphasis on luxury as we are looking to attract high end clients so not generic and something that is easily purchased from crafto
Nice to have
• need the following design scheme as it relates to color and font Primary Color Palette: 1. Ecru Stone (Soft Beige/Taupe) – #D7CCC0 • Evokes warmth, trust, and sophistication. 2. Slate Charcoal (Deep Neutral Gray) – #4A4A4A • Represents professionalism, authority, and reliability. Accent Colors: 3. Soft Gold (Understated Elegance) – #C2B280 • Adds a subtle richness without being flashy. 4. Powder White (Clean Background Base) – #FAF9F6 • Used for breathing room, high readability, and elegance. Typography/Callout Highlight Color: 5. Trust Blue (Soft Navy) – #3F4A5F • Often used for headers or key points to add credibility and depth. Tessa Varden should be in cursive, readable and absolutely beautiful
Should not have
• No yellow, do not use ai on my image,

```html
<!DOCTYPE html>
<html lang="en">
<head>
<meta charset="utf-8">
<title>Probate &amp; Trust Postcard – Tessa Varden</title>
<link href="https://fonts.googleapis.com/css2?family=Cinzel:wght@400;500;600&family=Great+Vibes&family=Poppins:wght@400;500;600;700&display=swap" rel="stylesheet">
<style>
  :root{
    --backdrop:#666666;
    --slate:#4a4a4a;
    --white:#ffffff;
    --gold:#a08a4e;
    --gold-soft:#c2b46e;
    --ink:#111111;
    --stamp:#e6e6e6;
    --rule:#a3a3a3;
  }
  *{box-sizing:border-box;margin:0;padding:0}
  html,body{width:839px;height:1200px;overflow:hidden;background:var(--backdrop)}
  body{position:relative;font-family:"Poppins",sans-serif;color:var(--ink)}
  .abs{position:absolute}
  .card{position:absolute;left:104px;width:631px;height:421px;box-shadow:0 2px 6px rgba(0,0,0,.25);overflow:hidden}
  .card--front{top:131px;background:var(--slate)}
  .card--back{top:648px;background:var(--white)}

  /* shared brand lockup */
  .brand-mark{width:40px;height:40px;border:1.5px solid var(--gold);border-radius:50%}
  .brand-name{text-align:center;font-family:"Cinzel",serif;font-size:14px;letter-spacing:.2px;color:#333;white-space:nowrap;line-height:1}
  .brand-title{text-align:center;font-family:"Cinzel",serif;font-size:7.5px;letter-spacing:4px;color:var(--gold);white-space:nowrap;line-height:1}

  /* FRONT */
  .front-panel{left:0;top:0;width:454px;height:421px;background:var(--white)}
  .front-column{left:20px;width:334px;text-align:center;white-space:nowrap}
  .headline{top:132px;font-family:"Cinzel",serif;font-weight:500;font-size:36px;line-height:1;letter-spacing:-.5px;color:var(--ink)}
  .headline-script{top:150px;font-family:"Great Vibes",cursive;font-size:32px;line-height:1;color:var(--gold);padding-left:4px}
  .headline-sub{top:188px;font-size:14.5px;font-weight:500;line-height:18px}
  .subhead{top:217px;font-size:11.2px;line-height:14px;font-weight:500}
  .headshot{left:37px;top:267px;width:93px;height:93px;border-radius:50%;background:radial-gradient(circle at 50% 40%,#8a6a55,#2e2a2a 70%);border:2px solid var(--white)}
  .agent-bar{left:128px;top:290px;width:178px;height:36px;background:var(--gold);border-radius:0 8px 8px 0}
  .agent-name{left:148px;top:290px;height:36px;line-height:37px;font-size:19px;font-weight:500;color:var(--white);white-space:nowrap}
  .agent-title{left:150px;top:332px;font-size:14px;font-weight:500;line-height:18px}
  .website{left:33px;top:367px;font-size:14px;font-weight:500;white-space:nowrap;line-height:18px}
  .website b{color:var(--gold);font-weight:600}

  .photo-frame{left:365px;top:30px;width:235px;height:255px;background:var(--white)}
  .photo{left:365px;top:36px;width:230px;height:244px;background:linear-gradient(160deg,#e9e6df 0%,#c9c2b4 40%,#6d6a62 70%,#3a3938 100%)}

  .names-tab{left:366px;top:302px;width:55px;height:17px;background:var(--gold);border-radius:6px 6px 0 0;color:var(--white);font-size:11px;line-height:18px;text-align:center}
  .names-box{left:359px;top:315px;width:239px;height:72px;background:var(--white);border:1px solid #9a9a9a;border-radius:0 0 10px 10px}
  .names-line{position:absolute;left:0;right:0;height:1px;background:var(--gold-soft)}

  /* BACK */
  .back-panel{left:0;top:0;width:345px;height:421px;background:var(--slate)}
  .back-band{left:0;top:316px;width:345px;height:105px;background:var(--gold-soft)}
  .quote-frame{left:36px;top:39px;width:254px;height:38px}
  .quote-text{left:36px;top:48px;width:254px;text-align:center;font-size:6.8px;line-height:8.4px;color:var(--white)}
  .quote-mark{font-weight:700;color:var(--white);font-size:12px;line-height:1;background:var(--slate);padding:0 2px}
  .body-copy{left:34px;width:290px;font-size:6.7px;line-height:8.3px;color:var(--white)}
  .offer{left:33px;top:194px;width:254px;height:38px;background:var(--gold-soft);border-radius:12px 0 12px 0;text-align:center;font-weight:700;font-size:11.3px;line-height:14px;padding-top:6px}
  .offer-top{color:var(--slate)}
  .offer-bottom{color:var(--white)}
  .offer-item{width:140px;font-size:6.8px;line-height:8.3px;color:var(--white);padding-left:9px}
  .offer-item::before{content:"";position:absolute;left:0;top:1.5px;width:5px;height:5px;border-radius:50%;background:var(--gold-soft)}
  .pull-tab{left:64px;top:302px}
  .pull{left:73px;top:306px;width:180px;height:29px;background:var(--white);font-weight:600;font-size:7.9px;line-height:10px;padding:4px 0 0 7px}
  .cta{left:0;width:345px;top:342px;text-align:center;font-weight:600;font-size:7.4px;line-height:9px}
  .pill{top:372px;height:16px;background:var(--white);border-radius:8px;font-size:9.2px;line-height:16px;padding-left:17px;font-weight:500;white-space:nowrap}
  .pill::before{content:"";position:absolute;left:5px;top:4px;width:8px;height:8px;border-radius:50%;background:var(--gold-soft)}
  .stamp{left:532px;top:33px;width:65px;height:64px;background:var(--stamp)}
  .addr-line{left:408px;width:191px;height:2px;background:var(--rule)}
</style>
</head>
<body>

<section class="card card--front" aria-label="Postcard front">
  <div class="abs front-panel"></div>

  <div class="abs brand-mark" style="left:167px;top:38px"></div>
  <div class="abs brand-name" style="left:20px;width:334px;top:91px">TESSA N. VARDEN</div>
  <div class="abs brand-title" style="left:20px;width:334px;top:109px">REALTOR®</div>

  <h1 class="abs front-column headline">YOU’VE TAKEN</h1>
  <div class="abs front-column headline-script">On So Much</div>
  <div class="abs front-column headline-sub">LET ME HELP WITH WHAT COMES NEXT</div>
  <p class="abs front-column subhead">Strategic Real Estate Guidance for Probate &amp; Trust<br>Certified Probate &amp; Trust Specialist | Serving<br>the San Francisco Bay Area</p>

  <div class="abs agent-bar"></div>
  <div class="abs headshot" role="img" aria-label="Headshot of Tessa Varden"></div>
  <div class="abs agent-name">Tessa Varden</div>
  <div class="abs agent-title">REALTOR®</div>
  <div class="abs website">www.<b>tessanvarden.halvenrealty</b>.com</div>

  <div class="abs photo-frame"></div>
  <div class="abs photo" role="img" aria-label="Bright, calm living room interior with sofa, coffee table and indoor tree"></div>

  <div class="abs names-box">
    <span class="names-line" style="top:14px"></span>
    <span class="names-line" style="top:28px"></span>
    <span class="names-line" style="top:42px"></span>
    <span class="names-line" style="top:56px"></span>
  </div>
  <div class="abs names-tab">NAMES</div>
</section>

<section class="card card--back" aria-label="Postcard back">
  <div class="abs back-panel"></div>
  <div class="abs back-band"></div>

  <svg class="abs quote-frame" width="254" height="38" viewBox="0 0 254 38" aria-hidden="true">
    <path d="M14 1 H253 V22 Q253 37 238 37 H5 M1 37 V16 Q1 1 16 1" fill="none" stroke="#c2b46e" stroke-width="1"/>
  </svg>
  <span class="abs quote-mark" style="left:49px;top:33px">“</span>
  <span class="abs quote-mark" style="left:262px;top:73px">”</span>
  <p class="abs quote-text">I lost both of my parents in 2020 — just weeks apart. That experience<br>shaped how I serve every estate I touch.</p>

  <p class="abs body-copy" style="top:94px">My name is Tessa Varden, and I’m a Certified Probate &amp; Trust Specialist who works with families, attorneys, and fiduciaries to guide the real estate side of probate with structure, sensitivity, and strategy.</p>
  <p class="abs body-copy" style="top:123px">Whether you’re navigating this with legal support or filing in pro per, this process is layered — emotional, procedural, and often overwhelming. I provide a steady hand when everything else feels uncertain.</p>
  <p class="abs body-copy" style="top:153px">With over a decade of experience supporting executives at Corvane, Lumirel, and Dunmore Pike, I bring the same operational precision and discretion to every estate I manage. But I also bring empathy — because I’ve been in your shoes.</p>

  <div class="abs offer"><div class="offer-top">WHAT I OFFER</div><div class="offer-bottom">AT NO UPFRONT COST TO THE ESTATE</div></div>

  <p class="abs offer-item" style="left:33px;top:245px">Property clean-outs, inspections, and basic preparation coordinated and covered</p>
  <p class="abs offer-item" style="left:33px;top:275px">Real estate strategy aligned with court timelines and estate goals</p>
  <p class="abs offer-item" style="left:185px;top:245px;width:150px">Hands-on collaboration with attorneys or step-by-step guidance for independent petitioners</p>
  <p class="abs offer-item" style="left:185px;top:275px">Thoughtful communication that honors your time and your grief</p>

  <svg class="abs pull-tab" width="200" height="15" viewBox="0 0 200 15" aria-hidden="true">
    <path d="M0 14 L9 4 H191 L200 14 Z" fill="#e3e3e3"/>
  </svg>
  <p class="abs pull">Because real estate isn’t just business.<br>For you, it’s personal. For me, it’s both.</p>

  <p class="abs cta">If you’re managing a probate or trust estate and need support you can trust<br>let’s make this easier, together.</p>

  <div class="abs pill" style="left:34px;width:93px">@itstessavoo</div>
  <div class="abs pill" style="left:142px;width:192px">profilehub.net/in/tessahomesagent</div>

  <div class="abs brand-mark" style="left:428px;top:33px"></div>
  <div class="abs brand-name" style="left:348px;width:200px;top:80px;font-size:12.5px">TESSA N. VARDEN</div>
  <div class="abs brand-title" style="left:348px;width:200px;top:96px;font-size:7px;letter-spacing:3.5px">REALTOR®</div>

  <div class="abs stamp" aria-label="Stamp area"></div>
  <div class="abs addr-line" style="top:190px"></div>
  <div class="abs addr-line" style="top:222px"></div>
  <div class="abs addr-line" style="top:255px"></div>
</section>

</body>
</html>
```